Summit Guest Partners

An Editable Business Card Template For SGP & SGH
Similar or Different Design

418 W. Marlow Ridge Pkwy.
Suite 2230
Irving, TX 75038

```html
<!DOCTYPE html>
<html lang="en">
<head>
<meta charset="utf-8">
<title>Summit Guest Partners – Business Cards</title>
<link rel="stylesheet" href="https://fonts.googleapis.com/css2?family=EB+Garamond:wght@400;500;600&display=swap">
<style>
  :root {
    --backdrop: #2c2c2c;
    --card: #f1f1f1;
    --wine: #8a2427;
    --wine-deep: #7a1e22;
    --ink: #1e1e1e;
    --band-text: #f4e9e9;
  }
  * { margin: 0; padding: 0; box-sizing: border-box; }
  html, body { width: 1200px; height: 1138px; overflow: hidden; }
  body {
    background: var(--backdrop);
    font-family: "EB Garamond", Garamond, serif;
    position: relative;
  }
  .card {
    position: absolute;
    width: 376px;
    height: 622px;
    background: var(--card);
    border-radius: 14px;
    overflow: hidden;
    transform: rotate(-90deg);
    text-align: center;
    color: var(--ink);
  }
  .card--company { left: 395px; top: 61px; }
  .card--personal { left: 397px; top: 483px; }

  .brand { position: absolute; top: 34px; left: 0; width: 100%; }
  .brand__mark {
    width: 132px; height: 132px; border-radius: 50%;
    background: var(--wine); margin: 0 auto;
  }
  .brand__name {
    margin-top: 14px; font-size: 19px; font-weight: 500;
    color: var(--wine); letter-spacing: 0.06em; font-variant: small-caps;
  }

  .line { position: absolute; left: 0; width: 100%; white-space: nowrap; }

  .office__label { top: 262px; font-size: 21px; }
  .office__phone { top: 286px; font-size: 31px; color: var(--wine); letter-spacing: 0.02em; }
  .office__address { top: 330px; font-size: 12.5px; }
  .pitch { font-size: 15.5px; color: var(--wine); }
  .pitch--1 { top: 382px; }
  .pitch--2 { top: 404px; }
  .feature { font-size: 15px; }
  .feature--1 { top: 436px; }
  .feature--2 { top: 459px; }
  .feature--3 { top: 482px; }
  .feature--4 { top: 505px; }
  .feature--5 { top: 528px; }

  .band {
    position: absolute; left: 0; bottom: 0; width: 100%; height: 50px;
    background: var(--wine-deep);
    color: var(--band-text);
    display: flex; align-items: center; justify-content: center;
    font-size: 17px; letter-spacing: 0.05em; font-variant: small-caps;
  }

  .person__name { top: 318px; font-size: 30px; font-weight: 600; color: var(--wine); }
  .person__role { top: 356px; font-size: 18px; }
  .contact-rule { position: absolute; top: 412px; left: 80px; width: 216px; height: 30px; }
  .contact { font-size: 17.5px; }
  .contact--1 { top: 458px; }
  .contact--2 { top: 481px; }
  .contact--3 { top: 504px; }
</style>
</head>
<body>

<section class="card card--company">
  <div class="brand">
    <div class="brand__mark"></div>
    <div class="brand__name">SGP · Summit Guest Partners</div>
  </div>
  <div class="line office__label">Corporate Office</div>
  <div class="line office__phone">214-555-0172</div>
  <div class="line office__address">418 W. Marlow Ridge Pkwy. St 2230 Irving, TX 75038</div>
  <div class="line pitch pitch--1">Trusted lodging partner for Energy,</div>
  <div class="line pitch pitch--2">Mining &amp; Infrastructure Work Crews.</div>
  <div class="line feature feature--1">Single Monthly Invoice</div>
  <div class="line feature feature--2">Furnished Crew Housing Nationwide</div>
  <div class="line feature feature--3">Around-the-Clock Booking Desk</div>
  <div class="line feature feature--4">Reliable Service on Every Project</div>
  <div class="line feature feature--5">Fair Pricing with Clear, Simple Terms</div>
  <div class="band">www.SGPCrewStays.com</div>
</section>

<section class="card card--personal">
  <div class="brand">
    <div class="brand__mark"></div>
    <div class="brand__name">SGH · Summit Guest Housing</div>
  </div>
  <div class="line person__name">Dana Whitfield</div>
  <div class="line person__role">Sales Manager</div>
  <svg class="contact-rule" viewBox="0 0 216 30" aria-hidden="true">
    <line x1="0" y1="15" x2="72" y2="15" stroke="#8a2427" stroke-width="1.5"/>
    <line x1="144" y1="15" x2="216" y2="15" stroke="#8a2427" stroke-width="1.5"/>
    <g fill="none" stroke="#8a2427" stroke-width="1.4">
      <circle cx="84" cy="15" r="10"/>
      <circle cx="108" cy="15" r="10"/>
      <circle cx="132" cy="15" r="10"/>
      <path d="M79 18 q5 -9 10 0 z"/>
      <rect x="102" y="11" width="12" height="8"/>
      <path d="M102 11 l6 5 l6 -5"/>
      <circle cx="132" cy="15" r="5"/>
      <path d="M127 15 h10 M132 10 v10"/>
    </g>
  </svg>
  <div class="line contact contact--1">214-555-0172</div>
  <div class="line contact contact--2">480-555-0143</div>
  <div class="line contact contact--3">dwhitfield@summitguest.com</div>
  <div class="band">Crew Lodging Made Simple</div>
</section>

</body>
</html>
```